Finiding oppertunites in Real Estate 6.15.20

size of ad 7” x 9.6”
1-I like the ad to stand out and attract people's attention.
2-you should be able to see the text of the ad clearly .. see the attachment anything in yellow is instructions.
3-the list of topics should not be the main part of the ad
4-if you decide you want a picture or vector of a person .. (you decide)
then it should be a white male about 25-30 years old wearing a solid white or blue shirt and not long hair.
5-leave 1 inch for footer
see attachment
Good luck

Target Market(s)

potential male students 25-35 years of age

Industry/Entity Type

Education

Requirements
Must have
• will stand out and people would want to see it.
should be able to read the words of ad
Nice to have
• how to make money in real estate on one line

```html
<!DOCTYPE html>
<html lang="en">
<head>
<meta charset="utf-8">
<title>How to Make Money in Real Estate – Course Poster</title>
<link rel="stylesheet" href="https://fonts.googleapis.com/css2?family=Poppins:wght@400;500;600;700&family=Oswald:wght@400;500&display=swap">
<style>
  :root {
    --navy: #1c3c7a;
    --navy-deep: #0f2452;
    --navy-glass: rgba(22, 48, 104, 0.82);
    --slate-top: #4b4c50;
    --slate-bottom: #77787c;
    --paper: #ffffff;
    --canvas: #ececec;
    --ink-light: #ffffff;
  }
  * { margin: 0; padding: 0; box-sizing: border-box; }
  html, body { width: 686px; height: 1200px; overflow: hidden; }
  body { background: var(--canvas); font-family: "Poppins", sans-serif; position: relative; }

  .poster {
    position: absolute; left: 23px; top: 160px;
    width: 640px; height: 880px;
    background: var(--paper);
    box-shadow: 0 10px 30px rgba(0,0,0,0.25);
    overflow: hidden;
  }
  .headline-band {
    position: absolute; left: 0; top: 0; width: 640px; height: 96px;
    display: flex; align-items: center; justify-content: center;
  }
  .headline-band h1 {
    font-weight: 500; font-size: 51px; color: var(--navy); letter-spacing: -0.3px; white-space: nowrap;
  }
  .stage {
    position: absolute; left: 0; top: 96px; width: 640px; height: 707px;
    background: linear-gradient(180deg, var(--slate-top), var(--slate-bottom));
    overflow: hidden;
  }
  .subhead {
    position: absolute; left: 66px; top: -6px; color: var(--ink-light); white-space: nowrap; line-height: 1.2;
  }
  .subhead .lead { font-size: 44px; font-weight: 400; }
  .subhead .key { font-size: 72px; font-weight: 700; letter-spacing: -0.5px; }

  .portrait {
    position: absolute; left: 210px; top: 56px; width: 340px; height: 651px;
    background: linear-gradient(180deg, #7e7f83 0%, #d9d9db 30%, #f1f1f2 60%, #c9cacc 100%);
    border-radius: 140px 140px 0 0;
  }
  .accent { position: absolute; left: 0; top: 0; }

  .pitch { position: absolute; left: 36px; top: 106px; width: 340px; }
  .pitch p {
    border-left: 4px solid var(--ink-light);
    padding-left: 20px; margin-bottom: 20px;
    color: var(--ink-light); font-size: 19px; line-height: 1.3;
  }

  .format-label {
    position: absolute; left: 32px; top: 252px; height: 186px;
    writing-mode: vertical-rl; transform: rotate(180deg);
    white-space: nowrap;
    font-family: "Oswald", sans-serif; font-weight: 500; font-size: 25px; line-height: 30px;
    color: var(--ink-light); text-align: center; letter-spacing: 0.3px;
  }
  .schedule { position: absolute; left: 80px; top: 282px; color: var(--ink-light); font-family: "Oswald", sans-serif; white-space: nowrap; }
  .schedule .small { font-size: 20px; font-weight: 400; line-height: 28px; display: flex; align-items: center; gap: 8px; }
  .schedule .small::before {
    content: ""; border-left: 10px solid var(--ink-light);
    border-top: 6px solid transparent; border-bottom: 6px solid transparent;
  }
  .schedule .big { font-size: 35px; font-weight: 500; line-height: 40px; margin: 0 0 10px 18px; }

  .topics {
    position: absolute; left: 23px; top: 474px; width: 305px; height: 233px;
    background: var(--navy-glass); padding: 30px 0 0 10px;
  }
  .topics ul { list-style: none; }
  .topics li {
    color: var(--ink-light); font-size: 13px; line-height: 20px; display: flex; gap: 9px; white-space: nowrap;
  }
  .topics li span::before {
    content: ""; display: inline-block; width: 6px; height: 6px; border-radius: 50%;
    background: var(--ink-light); margin-right: 8px; vertical-align: 2px;
  }
  .topics li span.hollow::before { background: none; border: 1px solid var(--ink-light); }

  .course-name {
    position: absolute; left: 578px; top: 300px;
    writing-mode: vertical-rl; white-space: nowrap;
    color: var(--ink-light); font-size: 26px; font-weight: 500;
  }

  .footer {
    position: absolute; left: 0; top: 803px; width: 640px; height: 77px;
    background: var(--paper);
  }
  .footer .rule-thick { position: absolute; left: 0; top: 2px; width: 640px; height: 5px; background: var(--navy); }
  .footer .rule-thin { position: absolute; left: 0; top: 11px; width: 640px; height: 2px; background: var(--navy); }
  .footer .site {
    position: absolute; left: 0; top: 38px; width: 640px; text-align: center;
    font-size: 16px; font-weight: 500; color: var(--navy);
  }
</style>
</head>
<body>
  <main class="poster">
    <header class="headline-band">
      <h1>How to Make Money</h1>
    </header>

    <section class="stage">
      <div class="portrait" role="img" aria-label="Photo of a man about 25–30 years old in a solid white shirt, arms crossed"></div>

      <svg class="accent" width="640" height="707" viewBox="0 0 640 707" aria-hidden="true">
        <polygon points="612,0 640,0 640,707 492,707" fill="var(--navy-deep)"/>
        <line x1="600" y1="20" x2="468" y2="707" stroke="#ffffff" stroke-width="3"/>
        <line x1="588" y1="40" x2="444" y2="707" stroke="var(--navy)" stroke-width="9"/>
      </svg>

      <div class="subhead"><span class="lead">In </span><span class="key">Real Estate?</span></div>

      <div class="pitch">
        <p>For those who have started or would like to go into Real Estate</p>
        <p>An investment in knowledge opens up untold opportunities</p>
      </div>

      <div class="format-label">REMOTE SESSIONS</div>
      <div class="schedule">
        <div class="small">12 SESSION</div>
        <div class="big">COURSE</div>
        <div class="small">CLASSES STARTING</div>
        <div class="big">JUNE 16</div>
      </div>

      <div class="topics">
        <ul>
          <li><span>A partial listing of Topics</span><span class="hollow">Single-family</span></li>
          <li><span>Multifamily</span><span class="hollow">Management</span></li>
          <li><span>Real Estate Concepts</span></li>
          <li><span>Real Estate law</span></li>
          <li><span>Investment properties</span></li>
          <li><span>Foreclosures</span><span class="hollow">Rehab</span><span class="hollow">Foreclosures</span></li>
          <li><span>Short sales</span><span class="hollow">Development</span></li>
          <li><span>Finical modeling</span><span class="hollow">HUD properties</span></li>
          <li><span>Due Diligence</span></li>
        </ul>
      </div>

      <div class="course-name">Real Estate Career Course</div>
    </section>

    <footer class="footer">
      <div class="rule-thick"></div>
      <div class="rule-thin"></div>
      <div class="site">www.website.com</div>
    </footer>
  </main>
</body>
</html>
```